Business Card Design Project

We are a tiling/bathroom renovation business based in Brisbane Australia and are looking to get a professional looking business card designed to promote ourselves.

We provide quality workmanship to upgrade/enhance peoples' homes.
Updates

Target Market(s)

Homeowners looking to renovate their bathrooms, or get tiling done. Mostly young adults to elderly who can spare several grand to upgrade their home

Industry/Entity Type

Business

Requirements
Must have
• A bold heading is a must: "Tiling Corvel & Dray"
Must include these details: "ABN: 41 938 106 274", "BSA Licence: 8073162", "Bastien: 0491 873 210", "Rhys: 0468 215 093", "Email: tilingcorvelanddray@quillmarsh.com", "Let Us Set It Straight".

An abstract geometrical logo that's based around squares and straight lines/arrows because we are a tiling business and our slogan is "Let Us Set It Straight"
Nice to have
• I have attached an image of a logo design I got from markvesta.com, and the background from Cardlorne.com.au templates I really like together I just need the cut and paste look ironed out.

You are free to play around with different looks and feels but around the same theme as my sample. i.e. simple but striking, minimal but eye catching, or not maybe something unexpected could be perfect who knows?
Should not have
• Photorealism on a business card is a pet peeve. Too much detail for a teeny tiny business card. A Business card should stand out at a distance and you shouldn't have to squint to see it's detail.

```html
<!DOCTYPE html>
<html lang="en">
<head>
<meta charset="utf-8">
<title>Tiling Corvel &amp; Dray — Business Card</title>
<link rel="stylesheet" href="https://fonts.googleapis.com/css2?family=Michroma&family=Lato:wght@400;700&display=swap">
<style>
  :root {
    --stage: #2e2e30;
    --card-light: #fbfbfb;
    --card-shade: #e6e6e8;
    --slate: #5d636c;
    --ink: #4a4f57;
    --amber: #e39a1c;
    --teal: #2eb3c6;
  }
  html, body {
    margin: 0;
    padding: 0;
    width: 1200px;
    height: 901px;
    overflow: hidden;
    background: var(--stage);
  }
  .card {
    position: absolute;
    left: 100px;
    top: 165px;
    width: 1000px;
    height: 571px;
    overflow: hidden;
    font-family: "Lato", sans-serif;
    color: var(--ink);
    box-shadow: 0 18px 40px rgba(0, 0, 0, 0.45);
  }
  .card-texture {
    position: absolute;
    inset: 0;
    background: linear-gradient(135deg, var(--card-light) 0%, var(--card-shade) 55%, var(--card-light) 100%);
  }
  .brand-heading {
    position: absolute;
    left: 58px;
    top: 58px;
    margin: 0;
    font-family: "Michroma", sans-serif;
    font-weight: 400;
    font-size: 38px;
    letter-spacing: 4px;
    text-transform: uppercase;
    color: var(--slate);
    white-space: nowrap;
  }
  .tagline {
    position: absolute;
    left: 112px;
    top: 116px;
    margin: 0;
    font-size: 18px;
    letter-spacing: 11px;
    text-transform: uppercase;
    color: var(--amber);
    white-space: nowrap;
  }
  .licence {
    position: absolute;
    left: 650px;
    top: 160px;
    font-size: 15px;
  }
  .brand-mark {
    position: absolute;
    left: 390px;
    top: 185px;
    width: 220px;
    display: flex;
    flex-direction: column;
    align-items: center;
    gap: 14px;
  }
  .brand-mark-square {
    width: 86px;
    height: 86px;
    border: 6px solid var(--amber);
    box-sizing: border-box;
  }
  .brand-mark-name {
    font-size: 20px;
    font-weight: 700;
    color: var(--teal);
    white-space: nowrap;
  }
  .abn {
    position: absolute;
    left: 82px;
    top: 322px;
    font-size: 15px;
  }
  .contact {
    position: absolute;
    font-size: 25px;
    white-space: nowrap;
  }
  .contact-label { color: var(--amber); }
  .contact-rhys { left: 650px; top: 298px; }
  .contact-email { left: 330px; top: 392px; font-size: 22px; }
  .contact-bastien { left: 60px; top: 440px; }
</style>
</head>
<body>
  <section class="card">
    <div class="card-texture" role="img" aria-label="Soft diamond tile pattern background"></div>

    <h1 class="brand-heading">Tiling Corvel &amp; Dray</h1>
    <p class="tagline">Let Us Set It Straight</p>

    <div class="licence">BSA Licence: 8073162</div>

    <div class="brand-mark">
      <div class="brand-mark-square"></div>
      <div class="brand-mark-name">Corvel &amp; Dray</div>
    </div>

    <div class="abn">ABN: 41 938 106 274</div>

    <div class="contact contact-rhys"><span class="contact-label">Rhys:</span> 0468 215 093</div>
    <div class="contact contact-email">Email: tilingcorvelanddray@quillmarsh.com</div>
    <div class="contact contact-bastien"><span class="contact-label">Bastien:</span> 0491 873 210</div>
  </section>
</body>
</html>
```